Redesign Business Cards, Attached

Please read instructions carefully. If you have any questions send a message before submitting your ONE design. Please redesign attached business cards. Double sided. Use same content and descriptions. Use black, silver, crimson red and gold colors. My only issue with the attached design is the background colors. I like the layout as-is. I can provide the individual pictures on the back side later. Do not submit more than one design. One submission shall include both front and back. Do not submit front and back separately. A second project will be launched to create a matching post card after completion of this.
Industry/Entity Type
see description and attachments.
Contact Information for Business Card
Requirements
Must have
- see description and attachments.
Nice to have
Should not have

```html
<!DOCTYPE html>
<html lang="en">
<head>
<meta charset="UTF-8">
<title>Harbor Helm Business Cards</title>
<link href="https://fonts.googleapis.com/css2?family=Montserrat:wght@400;600;700;800&display=swap" rel="stylesheet">
<style>
  :root {
    --page: #f2f2f2;
    --card-dark: #2a2b2f;
    --card-dark-2: #1f2023;
    --crimson: #c13a2c;
    --crimson-btn: #b6302a;
    --crimson-bar: #d8463a;
    --gold: #d4a93c;
    --white: #ffffff;
    --silver: #d9dde2;
    --sea-1: #9fb7c9;
    --sea-2: #e9f0f5;
  }
  * { margin: 0; padding: 0; box-sizing: border-box; }
  html, body { width: 1198px; height: 1200px; overflow: hidden; }
  body {
    background: var(--page);
    font-family: "Montserrat", Arial, sans-serif;
    color: var(--white);
    position: relative;
  }
  .card {
    position: absolute;
    left: 203px;
    width: 792px;
    height: 456px;
    border-radius: 36px;
    overflow: hidden;
  }
  .card--front { top: 106px; }
  .card--back { top: 644px; }
  .card__art { position: absolute; inset: 0; width: 792px; height: 456px; }

  .brand { position: absolute; display: flex; flex-direction: column; align-items: center; }
  .brand__dot { width: 46px; height: 46px; border-radius: 50%; background: var(--gold); }
  .brand__name { margin-top: 6px; font-weight: 700; font-size: 11px; letter-spacing: 1.5px; color: var(--white); }
  .card--front .brand { left: 144px; top: 36px; width: 120px; }
  .card--back .brand { left: 24px; top: 34px; width: 120px; }
  .card--back .brand__dot { width: 62px; height: 62px; }

  .site-url {
    position: absolute; left: 48px; top: 128px; width: 316px;
    text-align: center; font-weight: 700; font-size: 23px; letter-spacing: 0.2px;
  }

  .services { position: absolute; left: 42px; top: 176px; display: grid;
    grid-template-columns: 148px 148px; column-gap: 32px; row-gap: 19px; }
  .service {
    height: 41px; background: var(--crimson-btn); border-radius: 3px;
    border-left: 4px solid var(--crimson-bar);
    position: relative; padding-left: 16px; display: flex; align-items: center;
    font-weight: 700; font-size: 9px; line-height: 1.2; text-transform: uppercase;
  }
  .service::before { content: ""; position: absolute; left: 3px; top: 0; bottom: 0; width: 3px; background: var(--card-dark); }

  .person { position: absolute; left: 150px; top: 42px; }
  .person__name { font-weight: 800; font-size: 22px; letter-spacing: 0.6px; text-transform: uppercase; }
  .person__role { margin-top: 4px; font-size: 15px; line-height: 1.3; color: var(--silver); }

  .contacts { position: absolute; left: 64px; top: 164px; }
  .contact { display: flex; align-items: center; height: 50px; margin-bottom: 22px; }
  .contact__icon { width: 40px; height: 40px; margin-right: 14px; }
  .contact__text { border-left: 5px solid var(--crimson); padding-left: 10px; height: 48px;
    display: flex; flex-direction: column; justify-content: center; }
  .contact__label { font-weight: 700; font-size: 15px; text-transform: uppercase; }
  .contact__value { font-weight: 600; font-size: 15px; }
</style>
</head>
<body>

<!-- Front -->
<section class="card card--front">
  <svg class="card__art" viewBox="0 0 660 380" aria-hidden="false">
    <defs>
      <linearGradient id="seaFront" x1="0" y1="0" x2="1" y2="1">
        <stop offset="0" stop-color="var(--sea-1)"/>
        <stop offset="0.6" stop-color="var(--sea-2)"/>
        <stop offset="1" stop-color="#8aa3b6"/>
      </linearGradient>
    </defs>
    <rect width="660" height="380" fill="var(--card-dark)"/>
    <rect x="612" y="0" width="48" height="380" fill="var(--crimson)"/>
    <polygon points="470,18 612,90 612,290 470,362 328,290 328,90" fill="var(--crimson)" stroke="var(--crimson)" stroke-width="24" stroke-linejoin="round"/>
    <polygon points="470,34 596,98 596,282 470,346 344,282 344,98" fill="var(--card-dark-2)" stroke="var(--card-dark-2)" stroke-width="14" stroke-linejoin="round"/>
    <g role="img" aria-label="Photo of a white centre-console boat running across sparkling water">
      <polygon points="470,46 584,104 584,276 470,334 356,276 356,104" fill="url(#seaFront)" stroke="url(#seaFront)" stroke-width="12" stroke-linejoin="round"/>
    </g>
  </svg>

  <div class="brand"><span class="brand__dot"></span><span class="brand__name">HARBOR HELM</span></div>
  <p class="site-url">www.HireAHelmsman.com</p>

  <ul class="services">
    <li class="service">Hands-on<br>boat training</li>
    <li class="service">Island<br>anchoring</li>
    <li class="service">Introduction<br>to power boating</li>
    <li class="service">Open water<br>advanced<br>maneuvers</li>
    <li class="service">Precision docking &amp;<br>boat handling</li>
    <li class="service">Coastal<br>navigation</li>
    <li class="service">Open water<br>boat handling</li>
    <li class="service">Captaining / piloting<br>service for your<br>outings</li>
  </ul>
</section>

<!-- Back -->
<section class="card card--back">
  <svg class="card__art" viewBox="0 0 660 380">
    <defs>
      <linearGradient id="seaBack" x1="0" y1="0" x2="1" y2="1">
        <stop offset="0" stop-color="var(--sea-1)"/>
        <stop offset="0.6" stop-color="var(--sea-2)"/>
        <stop offset="1" stop-color="#8aa3b6"/>
      </linearGradient>
    </defs>
    <rect width="660" height="380" fill="var(--card-dark)"/>
    <rect x="0" y="324" width="660" height="56" fill="var(--crimson)"/>
    <polygon points="478,46 612,112 612,300 478,360 344,300 344,112" fill="var(--crimson)" stroke="var(--crimson)" stroke-width="24" stroke-linejoin="round"/>
    <polygon points="478,62 598,120 598,290 478,346 358,290 358,120" fill="var(--card-dark-2)" stroke="var(--card-dark-2)" stroke-width="14" stroke-linejoin="round"/>
    <g role="img" aria-label="Photo of a white centre-console boat cruising on open water">
      <polygon points="478,74 586,126 586,284 478,334 370,284 370,126" fill="url(#seaBack)" stroke="url(#seaBack)" stroke-width="12" stroke-linejoin="round"/>
    </g>
  </svg>

  <div class="brand"><span class="brand__dot"></span><span class="brand__name">HARBOR HELM</span></div>

  <div class="person">
    <h1 class="person__name">Dana R. Holloway</h1>
    <p class="person__role">USCG Licensed Captain<br>Certified Instructor</p>
  </div>

  <ul class="contacts">
    <li class="contact">
      <svg class="contact__icon" viewBox="0 0 40 40" fill="none" stroke="var(--white)" stroke-width="2.2" stroke-linejoin="round" stroke-linecap="round">
        <path d="M11 7 L16 7 L18 14 L14.5 16.5 Q17 23 23.5 25.5 L26 22 L33 24 L33 29 Q33 32 29 32 Q9 30 8 11 Q8 7 11 7 Z"/>
        <path d="M24 8 Q31 9 32 16"/><path d="M23 13 Q27 13.5 27.5 17"/>
      </svg>
      <div class="contact__text"><span class="contact__label">Phone</span><span class="contact__value">(555) 014-2290</span></div>
    </li>
    <li class="contact">
      <svg class="contact__icon" viewBox="0 0 40 40" fill="none" stroke="var(--white)" stroke-width="2.2" stroke-linejoin="round">
        <rect x="5" y="10" width="30" height="21" rx="1"/><path d="M5 10 L20 23 L35 10"/><path d="M5 31 L16 20 M35 31 L24 20"/>
      </svg>
      <div class="contact__text"><span class="contact__label">Email</span><span class="contact__value">hello@hireahelmsman.com</span></div>
    </li>
    <li class="contact">
      <svg class="contact__icon" viewBox="0 0 40 40" fill="none" stroke="var(--white)" stroke-width="2.2">
        <circle cx="20" cy="20" r="15"/><ellipse cx="20" cy="20" rx="6.5" ry="15"/><path d="M5 20 H35 M8 12 H32 M8 28 H32"/>
      </svg>
      <div class="contact__text"><span class="contact__label">Website</span><span class="contact__value">www.HireAHelmsman.com</span></div>
    </li>
  </ul>
</section>

</body>
</html>
```